An innovative software company needs a business card!

We need a business card design for our new innovative software company. Please use the details for the business card provided in business card details section. We will use the business card paper like: https://www.plavex.com/us/products/nfc/business-cards-plus.html Our company name: kelvora We have already a logo and colors to use in business cards too ,

Target Market(s)

App & Sofware Development

Industry/Entity Type

Software

Contact Information for Business Card

Lukas Brenner, BSc.
Owner and Creative Superhero

Adress:
Tulpenweg 37/4/1809
A - 1100, Wien

Tel: +43 (0) 676 921 35 60
Email: lukas.brenner@kelvora.at
Web: www.kelvora.at

Requirements
Must have
• - Use our logo
Nice to have
• It would be nice to have a nice picture on the backside. (About apps, software, technicals or funy stuff) - Use our colors as in business card (optional)

```html
<!DOCTYPE html>
<html lang="de">
<head>
<meta charset="utf-8">
<title>kelvora – Visitenkarte</title>
<link rel="stylesheet" href="https://fonts.googleapis.com/css2?family=Open+Sans:wght@400;600;700&display=swap">
<style>
  :root {
    --brand-blue: #1ca5cf;
    --brand-dark: #3d3d3d;
    --card-white: #ffffff;
    --backdrop: #e9e6e3;
    --text-light: #ffffff;
  }
  * { box-sizing: border-box; margin: 0; padding: 0; }
  html, body { width: 1200px; height: 900px; overflow: hidden; }
  body {
    position: relative;
    background: var(--backdrop);
    font-family: "Open Sans", Arial, sans-serif;
  }
  .card {
    position: absolute;
    background: var(--card-white);
    box-shadow: 0 6px 18px rgba(0,0,0,0.18);
    overflow: hidden;
  }
  .card--front { left: 238px; top: 62px; width: 555px; height: 343px; }
  .card--back  { left: 457px; top: 518px; width: 560px; height: 344px; }

  .front__panel { position: absolute; inset: 0; }
  .front__content { position: absolute; left: 30px; top: 32px; color: var(--text-light); }
  .front__name { font-size: 15.5px; font-weight: 700; letter-spacing: 0.1px; }
  .front__role { font-size: 13.5px; font-weight: 400; margin-top: 1px; }
  .front__address { position: absolute; left: 30px; top: 179px; color: var(--text-light); font-size: 13.5px; line-height: 20px; }
  .front__contacts { position: absolute; left: 30px; top: 233px; list-style: none; color: var(--text-light); font-size: 13.5px; line-height: 20px; }
  .front__contacts li { display: flex; align-items: center; gap: 8px; }
  .front__contacts svg { width: 11px; height: 11px; flex: none; }

  .back__brand {
    position: absolute; left: 0; right: 0; top: 132px;
    display: flex; align-items: center; justify-content: center; gap: 18px;
  }
  .brand__dot { width: 62px; height: 62px; border-radius: 50%; background: var(--brand-dark); }
  .brand__name { font-size: 58px; font-weight: 700; color: var(--brand-blue); letter-spacing: 0.5px; line-height: 1; }
  .back__footer {
    position: absolute; left: 0; right: 0; top: 278px;
    display: flex; align-items: center; gap: 12px;
  }
  .back__rule { flex: 1; height: 1px; background: var(--brand-blue); }
  .back__web { font-size: 15px; font-weight: 700; color: var(--brand-blue); }
</style>
</head>
<body>
  <section class="card card--front" aria-label="Vorderseite">
    <svg class="front__panel" width="555" height="343" viewBox="0 0 555 343" aria-hidden="true">
      <path d="M0 0 H400 C 300 60 290 270 410 343 H0 Z" fill="var(--brand-blue)"/>
    </svg>
    <div class="front__content">
      <p class="front__name">Lukas Brenner, BSc.</p>
      <p class="front__role">Owner and Creative Superhero</p>
    </div>
    <address class="front__address" style="font-style:normal">
      Tulpenweg 37/4/1809<br>A - 1100, Wien
    </address>
    <ul class="front__contacts">
      <li>
        <svg viewBox="0 0 24 24"><path fill="#fff" d="M6.6 10.8a15.1 15.1 0 0 0 6.6 6.6l2.2-2.2a1 1 0 0 1 1-.25 11.4 11.4 0 0 0 3.6.57 1 1 0 0 1 1 1V20a1 1 0 0 1-1 1A17 17 0 0 1 3 4a1 1 0 0 1 1-1h3.5a1 1 0 0 1 1 1c0 1.25.2 2.45.57 3.6a1 1 0 0 1-.25 1z"/></svg>
        +43 (0) 676 921 35 60
      </li>
      <li>
        <svg viewBox="0 0 24 24"><path fill="#fff" d="M2 5h20v14H2z"/><path fill="none" stroke="var(--brand-blue)" stroke-width="2" d="M2 5l10 8 10-8"/></svg>
        lukas.brenner@kelvora.at
      </li>
      <li>
        <svg viewBox="0 0 24 24"><circle cx="12" cy="12" r="10" fill="#fff"/><path fill="none" stroke="var(--brand-blue)" stroke-width="1.6" d="M2 12h20M12 2c3 3 3 17 0 20M12 2c-3 3-3 17 0 20"/></svg>
        www.kelvora.at
      </li>
    </ul>
  </section>

  <section class="card card--back" aria-label="Rückseite">
    <div class="back__brand">
      <span class="brand__dot" aria-hidden="true"></span>
      <span class="brand__name">kelvora</span>
    </div>
    <div class="back__footer">
      <span class="back__rule"></span>
      <span class="back__web">www.kelvora.at</span>
      <span class="back__rule"></span>
    </div>
  </section>
</body>
</html>
```